Brent Oakes Director / Photographer Branding

I need note pads, envelops, business cards and letter head for my company. I'm a fashion and advertising director / photographer. I'm having trouble deciding how to include both Director & Photographer in my title or if it is even necessary. Maybe just my name is enough. I'm open for even using my initials if it works with the design and overall pieces. Please view my website to see what I have at this moment and what work I do. www.brentoakesstudio-mail.net
Updates

Project Deadline Extended
Reason: Hello Everyone! I'm extending the deadline since I have been traveling on a job out of country and I wanted to have more time to look through all the designs and give enough time for everyone to provide changes with designs and updates. I will be more available to communicate online now that I'm back in the office! Thank you! Brent Oakes

Target Market(s)

Fashion magazines, clothing lines and beauty cosmetic brands.

Industry/Entity Type

Fashion Photography

Font styles to use
Sans Serif

Colors
acd036
acd35d
cbcbcb
f5f5f5

Requirements
Must have
• My name.. Brent Oakes, my website: brentoakesstudio-mail.net my phone number, 555-284-6103
• I don't need my address on these. I also live by the philosophy that less is more and keeping things simple ads strength to a design. I also don't want to stop people from taking chances and experimenting with an idea that might take me down different road with my branding.
Nice to have
• Bold designs and clean lines. I'm open to ideas that I could adopt but I lean towards a more minimalistic look in general.
Should not have
• Not have cheesy graphics or pictures. No images of cameras, film or anything that looks like it is a camera or aperture, lens etc... ;)

```html
<!DOCTYPE html>
<html lang="en">
<head>
<meta charset="utf-8">
<title>Brent Oakes — Stationery</title>
<link href="https://fonts.googleapis.com/css2?family=Raleway:wght@200;400&display=swap" rel="stylesheet">
<style>
  :root{
    --green:#4f9f00;
    --paper:#f1f1f1;
    --backdrop:#b8b8b8;
    --ink:#6b6b6b;
    --ghost:#e2e2e2;
    --rule:#cfcfcf;
    --white:#ffffff;
    --soft-white:#dfeecf;
  }
  *{margin:0;padding:0;box-sizing:border-box}
  html,body{width:1200px;height:1200px;overflow:hidden}
  body{background:var(--backdrop);font-family:"Raleway",sans-serif;position:relative}
  .piece{position:absolute;background:var(--paper);overflow:hidden}

  .wordmark{position:absolute;display:flex;align-items:center;gap:.4em;color:var(--green);font-weight:400;line-height:1;letter-spacing:.06em;text-transform:uppercase;white-space:nowrap}
  .wordmark::before{content:"";width:.5em;height:.5em;background:currentColor;flex:none}
  .wordmark.light{color:var(--white)}

  .ghost{position:absolute;color:var(--ghost);font-weight:200;text-transform:uppercase;white-space:nowrap;line-height:1}
  .contact{position:absolute;color:var(--ink);font-size:4.6px;line-height:1.45;letter-spacing:.02em;white-space:nowrap}
  .accent{position:absolute;background:var(--green)}
  .flap{position:absolute;left:0;right:0;top:0;background:var(--green);border-radius:0 0 6px 6px;display:flex;align-items:center;justify-content:center;color:var(--white);font-size:6px;letter-spacing:.03em}
  .site{position:absolute;color:var(--soft-white);font-size:3.8px;white-space:nowrap}

  .letterhead{left:158px;top:84px;width:407px;height:528px}
  .letterhead .wordmark{left:24px;top:24px;font-size:16px}
  .letterhead .ghost{font-size:60px;left:360px;top:516px;transform:rotate(-90deg);transform-origin:0 0}
  .letterhead .contact{left:25px;top:480px}
  .letterhead .accent{left:0;top:481px;width:6px;height:24px}

  .envelope-front-a{left:614px;top:46px;width:452px;height:262px}
  .envelope-front-a .flap{height:60px;font-size:5px}
  .envelope-front-a .wordmark{left:17px;top:84px;font-size:16px}
  .envelope-front-a .ghost{font-size:54px;left:10px;top:222px}

  .envelope-back-pattern{left:614px;top:348px;width:452px;height:264px}
  .envelope-back-pattern .flap-pattern{position:absolute;left:0;top:0;width:452px;height:96px}

  .envelope-front-b{left:112px;top:660px;width:453px;height:203px}
  .envelope-front-b .wordmark{left:17px;top:20px;font-size:16px}
  .envelope-front-b .ghost{font-size:54px;left:10px;top:160px}

  .envelope-back-b{left:614px;top:661px;width:451px;height:203px}
  .envelope-back-b .flap{height:60px}

  .card-front{left:199px;top:908px;width:175px;height:96px}
  .card-front .wordmark{right:12px;top:70px;font-size:9px}
  .card-front .contact{left:14px;top:64px;font-size:3.8px}
  .card-front .accent{left:0;top:66px;width:4px;height:20px}

  .card-back{left:198px;top:1030px;width:175px;height:98px;background:var(--green)}
  .card-back .wordmark{left:12px;top:62px;font-size:12px}
  .card-back .site{left:13px;top:82px;font-size:3.6px}

  .notebook{left:415px;top:908px;width:149px;height:242px;background:var(--green);overflow:visible}
  .notebook .wordmark{right:14px;top:42px;font-size:11px}
  .notebook .site{right:14px;top:224px}
  .spiral{position:absolute;left:-6px;top:6px}

  .notepad{left:612px;top:908px;width:148px;height:242px;overflow:visible}
  .notepad .wordmark{left:16px;top:16px;font-size:8.5px}
  .notepad .contact{right:10px;top:11px;font-size:3.4px;text-align:right}
  .notepad .accent{right:0;top:13px;width:4px;height:18px}
  .notepad .lines{position:absolute;left:16px;right:12px;top:44px;bottom:12px;
    background:repeating-linear-gradient(to bottom,transparent 0 12.3px,var(--rule) 12.3px 13.3px)}

  .sticky{left:796px;top:908px;width:147px;height:147px}
  .sticky .wordmark{right:14px;top:16px;font-size:9px}
  .sticky .accent{right:0;top:12px;width:4px;height:18px}
</style>
</head>
<body>

  <section class="piece letterhead">
    <div class="wordmark">Brent Oakes</div>
    <div class="ghost">Brent Oakes</div>
    <div class="accent"></div>
    <div class="contact">BRENT OAKES PHOTOGRAPHER<br>555-284-6103<br>brent@brentoakesstudio-mail.net<br>www.brentoakesstudio-mail.net</div>
  </section>

  <section class="piece envelope-front-a">
    <div class="flap">www.brentoakesstudio-mail.net</div>
    <div class="wordmark">Brent Oakes</div>
    <div class="ghost">Brent Oakes</div>
  </section>

  <section class="piece envelope-back-pattern">
    <svg class="flap-pattern" viewBox="0 0 452 96" role="img" aria-label="Envelope liner flap with repeated name pattern in green">
      <path d="M0 6 Q0 0 6 0 H446 Q452 0 452 6 V96 H0 Z" fill="var(--green)"/>
      <path d="M0 72 Q14 68 22 84 Q30 96 40 96 H0 Z" fill="var(--paper)"/>
      <path d="M452 72 Q438 68 430 84 Q422 96 412 96 H452 Z" fill="var(--paper)"/>
    </svg>
  </section>

  <section class="piece envelope-front-b">
    <div class="wordmark">Brent Oakes</div>
    <div class="ghost">Brent Oakes</div>
  </section>

  <section class="piece envelope-back-b">
    <div class="flap">www.brentoakesstudio-mail.net</div>
  </section>

  <section class="piece card-front">
    <div class="accent"></div>
    <div class="contact">PHOTOGRAPHER | DIRECTOR<br>555-284-6103<br>brent@brentoakesstudio-mail.net<br>www.brentoakesstudio-mail.net</div>
    <div class="wordmark">Brent Oakes</div>
  </section>

  <section class="piece card-back">
    <div class="wordmark light">Brent Oakes</div>
    <div class="site">www.brentoakesstudio-mail.net</div>
  </section>

  <section class="piece notebook">
    <svg class="spiral" width="14" height="232" viewBox="0 0 14 232">
      <g fill="none" stroke="#8a8a8a" stroke-width="1.6">
        <path d="M2 4 h10 M2 19 h10 M2 34 h10 M2 49 h10 M2 64 h10 M2 79 h10 M2 94 h10 M2 109 h10 M2 124 h10 M2 139 h10 M2 154 h10 M2 169 h10 M2 184 h10 M2 199 h10 M2 214 h10 M2 229 h10"/>
      </g>
    </svg>
    <div class="wordmark light">Brent Oakes</div>
    <div class="site">www.brentoakesstudio-mail.net</div>
  </section>

  <section class="piece notepad">
    <svg class="spiral" width="14" height="232" viewBox="0 0 14 232">
      <g fill="none" stroke="#8a8a8a" stroke-width="1.6">
        <path d="M2 4 h10 M2 19 h10 M2 34 h10 M2 49 h10 M2 64 h10 M2 79 h10 M2 94 h10 M2 109 h10 M2 124 h10 M2 139 h10 M2 154 h10 M2 169 h10 M2 184 h10 M2 199 h10 M2 214 h10 M2 229 h10"/>
      </g>
    </svg>
    <div class="wordmark">Brent Oakes</div>
    <div class="contact">PHOTOGRAPHER | DIRECTOR<br>555-284-6103<br>brent@brentoakesstudio-mail.net<br>www.brentoakesstudio-mail.net</div>
    <div class="accent"></div>
    <div class="lines"></div>
  </section>

  <section class="piece sticky">
    <div class="wordmark">Brent Oakes</div>
    <div class="accent"></div>
  </section>

</body>
</html>
```